Fence Flyer to Attract More Sales During Winter

We need a new flyer made that we can distribute to residential mailboxes. The flyer is to promote our Winter Fence Sale. We like simply designs, and we would like the flyer to showcase a lot of our fence photos. More of our photos are online at our website at www.mybrindlewoodfence.com - our new address needs to also be featured on the flyer - 574 Quarry rd, Monroe, NC 28117. I do want the words "WINTER FENCE SALE" to be dominate on the flyer with the description "Wood fences starting at $12/FT!" Please look through our Facebook page and our website to gather more photos or information. We are flexible on colors, nothing to fancy - simple flyer design please.

Target Market(s)

Residential homeowners that need a new fence to enclose their yard for safety, security or decorative

Industry/Entity Type

Residential Construction

Font styles to use
Sans Serif

Colors

Designer to choose colors to be used in the design.

Requirements
Must have
• Winter Fence Sale
• Contact information for the business
• "Come visit our outdoor showroom, open 24/7!"
Nice to have
• Photos of our fences - you can find more on our website at www.MyBrindlewoodFence.com or Facebook.com/MapleholtFenceWBT
Should not have
• Flashy designs

```html
<!DOCTYPE html>
<html lang="en">
<head>
<meta charset="utf-8">
<title>Winter Fence Sale Flyer</title>
<link href="https://fonts.googleapis.com/css2?family=Anton&family=Exo+2:wght@700&family=Roboto+Condensed:wght@400;700&display=swap" rel="stylesheet">
<style>
:root{
  --red:#bb1e2d;
  --black:#1e1c1d;
  --brown:#4a2f16;
  --blue:#2f7fc4;
  --paper:#ffffff;
  --paper-low:#e3e3e5;
  --stage:#ececec;
}
*{margin:0;padding:0;box-sizing:border-box}
html,body{width:1040px;height:1200px;overflow:hidden;background:var(--stage)}
.flyer{
  position:absolute;left:70px;top:19px;width:966px;height:1248px;
  transform:scale(.931);transform-origin:0 0;
  background:linear-gradient(#fff 45%,var(--paper-low));
  font-family:"Roboto Condensed",sans-serif;color:var(--black);overflow:hidden;
}
.header-shape{position:absolute;left:0;top:0}
.brand{position:absolute;left:76px;top:104px;display:flex;align-items:center;gap:16px}
.brand-square{width:70px;height:70px;background:var(--brown);flex:none}
.brand-name{font-family:"Exo 2",sans-serif;font-weight:700;font-size:29px;color:var(--blue);line-height:1.1}
.brand-phone{font-family:"Exo 2",sans-serif;font-weight:700;font-size:35px;color:var(--black);line-height:1.15}
.brand-tagline{font-family:"Exo 2",sans-serif;font-weight:700;font-size:13px;color:var(--black);margin-top:4px;white-space:nowrap}
.title{position:absolute;left:500px;top:74px;font-family:"Anton",sans-serif;line-height:1;font-weight:400}
.title-top,.title-bottom{display:block;transform:scaleX(1.2);transform-origin:0 0;white-space:nowrap}
.title-top{font-size:92px;color:var(--black)}
.title-bottom{font-size:64px;color:var(--red);margin-top:6px}
.chevrons{position:absolute;left:855px;top:85px}
.style{position:absolute;width:230px}
.style-label{display:flex;align-items:center;gap:18px;font-size:17px;height:36px}
.style-num{width:36px;height:36px;border-radius:50%;color:#fff;font-family:"Anton",sans-serif;font-size:24px;display:flex;align-items:center;justify-content:center;flex:none}
.num-black{background:var(--black)}
.num-red{background:var(--red)}
.label-red{color:var(--red)}
.style-photo{position:absolute;top:46px;width:174px;height:174px;border-radius:50%;border:5px solid var(--brown)}
.ring-red{border-color:var(--red)}
.style-shadow{position:absolute;top:222px;width:190px;height:14px;border-radius:50%;background:radial-gradient(rgba(0,0,0,.22),transparent 70%)}
.photo-lawn{background:radial-gradient(circle at 50% 30%,#7aa256,#c9a774 75%)}
.photo-house{background:radial-gradient(circle at 50% 30%,#d8d5cc,#cdb48a 70%)}
.photo-wood{background:radial-gradient(circle at 40% 40%,#d7c197,#8a7b52 80%)}
.photo-sky{background:linear-gradient(#6f9bd6 20%,#d9c79b 55%,#a9a295)}
.photo-garden{background:radial-gradient(circle at 60% 40%,#bda37a,#3f6b31 80%)}
.photo-iron{background:radial-gradient(circle at 50% 40%,#6f9a4e,#2d3a22 85%)}
.photo-porch{background:radial-gradient(circle at 50% 60%,#e1b77a,#8c6a4c 80%)}
.address{position:absolute;left:56px;top:988px;display:flex;align-items:center;gap:16px}
.address-tag{background:var(--red);color:#fff;font-weight:700;font-size:31px;padding:2px 24px;border-radius:4px;height:50px;display:flex;align-items:center}
.address-text{font-size:32px}
.address-text b{font-weight:700}
.offer{position:absolute;left:58px;top:1062px;font-family:"Anton",sans-serif;font-size:66px;line-height:1;color:var(--red);white-space:nowrap;letter-spacing:-.5px}
.offer span{color:var(--black);font-size:78px}
.showroom{position:absolute;left:0;width:100%;top:1142px;text-align:center;font-size:22px;line-height:1.2}
.showroom b{color:var(--red)}
.footer{position:absolute;left:0;bottom:0;width:100%;height:74px;background:var(--black);color:#fff;font-size:27px;display:flex;align-items:center;justify-content:center}
</style>
</head>
<body>
<main class="flyer">
  <svg class="header-shape" width="966" height="140" viewBox="0 0 966 140">
    <path d="M0 0H966V40H484V128C420 90 350 62 270 60C150 58 60 95 0 138Z" fill="#bb1e2d"/>
    <path d="M0 138C60 95 150 58 270 60C350 62 420 90 484 128" fill="none" stroke="#1e1c1d" stroke-width="6"/>
    <path d="M0 24C90 24 200 36 270 56" fill="none" stroke="#1e1c1d" stroke-width="5"/>
    <path d="M484 44H966" stroke="#1e1c1d" stroke-width="3"/>
  </svg>

  <div class="brand">
    <div class="brand-square"></div>
    <div>
      <div class="brand-name">Brindlewood Fence</div>
      <div class="brand-phone">704-555-0142</div>
      <div class="brand-tagline">"Because Good Fences Make Good Neighbors"</div>
    </div>
  </div>

  <h1 class="title">
    <span class="title-top">WINTER</span>
    <span class="title-bottom">FENCE SALE</span>
  </h1>

  <svg class="chevrons" width="60" height="965" viewBox="0 0 60 965">
    <defs><path id="chev" d="M0 0L30 14L60 0V22L30 36L0 22Z"/></defs>
    <g>
      <use href="#chev" y="0" fill="#1e1c1d"/><use href="#chev" y="38" fill="#bb1e2d"/>
      <use href="#chev" y="76" fill="#1e1c1d"/><use href="#chev" y="114" fill="#bb1e2d"/>
      <use href="#chev" y="152" fill="#1e1c1d"/><use href="#chev" y="190" fill="#bb1e2d"/>
      <use href="#chev" y="228" fill="#1e1c1d"/>
    </g>
    <g>
      <use href="#chev" y="310" fill="#bb1e2d"/><use href="#chev" y="348" fill="#1e1c1d"/>
      <use href="#chev" y="386" fill="#bb1e2d"/><use href="#chev" y="424" fill="#1e1c1d"/>
      <use href="#chev" y="462" fill="#bb1e2d"/><use href="#chev" y="500" fill="#1e1c1d"/>
      <use href="#chev" y="538" fill="#bb1e2d"/><use href="#chev" y="576" fill="#1e1c1d"/>
    </g>
    <g>
      <use href="#chev" y="650" fill="#bb1e2d"/><use href="#chev" y="688" fill="#1e1c1d"/>
      <use href="#chev" y="726" fill="#bb1e2d"/><use href="#chev" y="764" fill="#1e1c1d"/>
      <use href="#chev" y="802" fill="#bb1e2d"/><use href="#chev" y="840" fill="#1e1c1d"/>
      <use href="#chev" y="878" fill="#bb1e2d"/><use href="#chev" y="916" fill="#1e1c1d"/>
    </g>
  </svg>

  <section class="styles">
    <div class="style" style="left:73px;top:262px">
      <div class="style-label"><span class="style-num num-black">1</span><span class="label-red">Split Rail Fence</span></div>
      <div class="style-photo photo-lawn" style="left:33px" role="img" aria-label="Photo of a wooden split rail fence with picket panel on a lawn"></div>
      <div class="style-shadow" style="left:25px"></div>
    </div>
    <div class="style" style="left:326px;top:262px">
      <div class="style-label"><span class="style-num num-black">2</span><span class="label-red">Brindlewood Picket</span></div>
      <div class="style-photo photo-house" style="left:33px" role="img" aria-label="Photo of a scalloped wood picket fence beside a house"></div>
      <div class="style-shadow" style="left:25px"></div>
    </div>
    <div class="style" style="left:569px;top:262px">
      <div class="style-label"><span class="style-num num-black">3</span><span class="label-red">Split Rail Fence</span></div>
      <div class="style-photo photo-lawn" style="left:33px" role="img" aria-label="Photo of a split rail fence with a wooden gate along trees"></div>
      <div class="style-shadow" style="left:25px"></div>
    </div>

    <div class="style" style="left:73px;top:500px">
      <div class="style-label"><span class="style-num num-red">4</span><span>Top Cap Privacy</span></div>
      <div class="style-photo photo-wood ring-red" style="left:24px" role="img" aria-label="Photo of a top cap wood privacy fence with gate"></div>
      <div class="style-shadow" style="left:16px"></div>
    </div>
    <div class="style" style="left:326px;top:500px">
      <div class="style-label"><span class="style-num num-red">5</span><span>Wood Dog Ear Picket</span></div>
      <div class="style-photo photo-sky ring-red" style="left:24px" role="img" aria-label="Photo of a dog ear wood picket fence in front of a brick house"></div>
      <div class="style-shadow" style="left:16px"></div>
    </div>
    <div class="style" style="left:569px;top:500px">
      <div class="style-label"><span class="style-num num-red">6</span><span>Wood Dog Ear Privacy</span></div>
      <div class="style-photo photo-garden ring-red" style="left:24px" role="img" aria-label="Photo of a dog ear wood privacy fence behind garden shrubs"></div>
      <div class="style-shadow" style="left:16px"></div>
    </div>

    <div class="style" style="left:73px;top:739px">
      <div class="style-label"><span class="style-num num-black">7</span><span class="label-red">Flat Top With Spears</span></div>
      <div class="style-photo photo-iron" style="left:24px" role="img" aria-label="Photo of a black metal flat top fence with spears in a garden"></div>
      <div class="style-shadow" style="left:16px"></div>
    </div>
    <div class="style" style="left:326px;top:739px">
      <div class="style-label"><span class="style-num num-black">8</span><span class="label-red">French Gothic Picket</span></div>
      <div class="style-photo photo-porch" style="left:24px" role="img" aria-label="Photo of a French gothic wood picket fence by a porch"></div>
      <div class="style-shadow" style="left:16px"></div>
    </div>
    <div class="style" style="left:569px;top:739px">
      <div class="style-label"><span class="style-num num-black">9</span><span class="label-red">Staggered Spear</span></div>
      <div class="style-photo photo-iron" style="left:24px" role="img" aria-label="Photo of a black staggered spear metal fence on a lawn"></div>
      <div class="style-shadow" style="left:16px"></div>
    </div>
  </section>

  <div class="address">
    <div class="address-tag">Our new address</div>
    <div class="address-text">574 Quarry rd, Monroe, <b>NC 28117</b></div>
  </div>

  <p class="offer">Wood fences starting at <span>$12/FT!</span></p>
  <p class="showroom">To see many more styles, come visit our outdoor showroom, <b>open 24/7!</b></p>

  <footer class="footer">www.mybrindlewoodfence.com</footer>
</main>
</body>
</html>
```